Dawson's Lawn Service needs a postcard design

I need a design to attract lawn cutting customers. I am a high school junior, focusing on my city and the neighboring city. I think it would be advantageous to let my potential clients know I am earning money for my college education. They should also know, I will be working side by side with my father, who operated his own lawn service for 20 years, so they can be assured of a quality result for their lawn. I will be using state of the art, commercial equipment.

A few things that are unique to my service are; my mower weighs half of what other commercial mowers do (a softer footprint), my mower does NOT throw clippings into mulch or flower beds, at an additional charge I offer bagging of the clippings and/or dog waste clean-up. I am thinking about a two-sided design. I would also like a cartoon style picture of myself riding my mower. If this is something you can create, I can send you a photo of myself and a photo of my mower. If not, I can get this drawing done separately, then send it to you, I would just need to know what kind of file you would need it in. I am not going to have a business name, I want to introduce myself as Dawson to keep it simple and personal. We can add a coupon to the postcard, offering one free cut with commitment to a full 26 week season. The name of my high school is Marwick High.

The cartoon picture attached is our logo.

Target Market(s)

Homeowners that use a commercial lawn cutting service, homeowners that need a temporary service while they are on vacation

Industry/Entity Type

School

Colors
3176b5
9bcb3c

Requirements
Must have
• An appeal for people to want to help me earn money for my college education. A clear idea they will be getting top notch service. I definitely want a drawing of myself on my mower. Phone # 555-271-0936
• design must work with parcelrelay.com/routeblanketmail guidelines

```html
<!DOCTYPE html>
<html lang="en">
<head>
<meta charset="utf-8">
<title>Dawson Mower – Postcard</title>
<link rel="stylesheet" href="https://fonts.googleapis.com/css2?family=Open+Sans:ital,wght@0,300;0,400;0,600;0,700;1,400;1,600&display=swap">
<style>
  :root {
    --charcoal: #2a2a2a;
    --navy: #0b4468;
    --olive: #a29c3f;
    --lime: #9bcb3c;
    --sky: #3d8fd1;
    --white: #ffffff;
    --ink: #333333;
    --rule: #9a9a9a;
    --grass-dark: #2f6a1c;
    --grass-light: #6fae35;
  }
  * { margin: 0; padding: 0; box-sizing: border-box; }
  html, body { width: 882px; height: 1200px; overflow: hidden; background: var(--white); }
  body { font-family: "Open Sans", Arial, sans-serif; color: var(--ink); position: relative; }

  .card { position: absolute; left: 0; width: 882px; overflow: hidden; }
  .card--front { top: 0; height: 588px; background: var(--charcoal); }
  .card--back { top: 612px; height: 588px; }
  .card svg.shapes { position: absolute; inset: 0; }
  .abs { position: absolute; }

  .wordmark { font-weight: 300; font-size: 50px; line-height: 1; letter-spacing: -1px; }
  .wordmark__school { font-size: 13px; letter-spacing: 2.6px; font-weight: 400; margin-top: 2px; }
  .card--front .wordmark, .card--front .wordmark__school { color: var(--white); }
  .card--back .wordmark, .card--back .wordmark__school { color: var(--navy); }

  .appeal { left: 515px; top: 24px; color: var(--white); font-size: 16px; }
  .callout { left: 515px; top: 45px; color: var(--lime); font-size: 20px; font-weight: 700; }

  .features { left: 36px; top: 127px; }
  .features__title { color: var(--sky); font-size: 19px; text-decoration: underline; text-underline-offset: 3px; font-weight: 400; margin-bottom: 20px; }
  .features__list { list-style: none; color: var(--white); font-size: 14px; line-height: 17px; }
  .features__list li { position: relative; padding-left: 34px; margin-bottom: 16px; width: 300px; }
  .features__list li svg { position: absolute; left: 5px; top: 2px; }
  .features__note { display: block; font-size: 11px; font-style: italic; }

  .offer { left: 140px; top: 544px; color: var(--white); font-size: 21px; white-space: nowrap; }
  .offer__label { text-decoration: underline; text-underline-offset: 3px; }
  .offer__text { font-style: italic; font-weight: 600; }

  .photo-slot { left: 140px; top: 44px; width: 208px; height: 294px; background: var(--white); border: 1px solid #bbb; display: flex; align-items: center; justify-content: center; font-size: 15px; }
  .stamp { left: 735px; top: 38px; width: 107px; height: 105px; background: var(--white); border: 1px solid #bbb; display: flex; align-items: center; justify-content: center; font-size: 11px; }
  .address { left: 523px; top: 205px; width: 315px; font-size: 15px; }
  .address__line { border-bottom: 1px solid var(--rule); height: 41px; padding: 8px 0 0 5px; }
  .address__line:first-child { height: 33px; padding-top: 0; }
  .address__blank { margin-left: 8px; height: 40px; border-bottom: 1px solid var(--rule); }
  .note-lines { left: 30px; top: 429px; width: 315px; }
  .note-lines span { display: block; height: 37.5px; border-bottom: 1px solid var(--rule); }
</style>
</head>
<body>

<section class="card card--front">
  <svg class="shapes" width="882" height="588" viewBox="0 0 882 588">
    <defs>
      <linearGradient id="lawnTone" x1="0" y1="0" x2="1" y2="1">
        <stop offset="0" stop-color="#23461a"/>
        <stop offset="0.45" stop-color="#5ea12e"/>
        <stop offset="1" stop-color="#1f3a16"/>
      </linearGradient>
    </defs>
    <path role="img" aria-label="Photo of a red zero-turn mower cutting a green lawn" fill="url(#lawnTone)"
          d="M585,82 L882,82 L882,588 L0,588 C120,420 360,190 585,82 Z"/>
    <path fill="var(--olive)" d="M0,470 C70,520 110,515 125,515 L125,588 L0,588 Z"/>
    <path fill="var(--navy)" d="M115,515 C330,500 640,480 882,415 L882,588 L115,588 Z"/>
    <circle cx="140" cy="437" r="70" fill="var(--charcoal)"/>
    <circle role="img" aria-label="Cartoon of Dawson riding his mower" cx="140" cy="437" r="59" fill="#2f7bbf"/>
  </svg>

  <div class="abs" style="left:33px; top:24px;">
    <div class="wordmark">DAWSON MOWER</div>
    <div class="wordmark__school">MARWICK HIGH SCHOOL</div>
  </div>

  <p class="abs appeal">Help me earn money for my college education.</p>
  <p class="abs callout">Call us on:&nbsp; # 555-271-0936</p>

  <div class="abs features">
    <h2 class="features__title">FEATURES WE OFFER</h2>
    <ul class="features__list">
      <li><svg width="11" height="10" viewBox="0 0 11 10"><path d="M1,5 L4,8.5 L10,1" fill="none" stroke="#fff" stroke-width="2"/></svg>a softer footprint</li>
      <li><svg width="11" height="10" viewBox="0 0 11 10"><path d="M1,5 L4,8.5 L10,1" fill="none" stroke="#fff" stroke-width="2"/></svg>does NOT throw clippings into mulch or flower beds</li>
      <li><svg width="11" height="10" viewBox="0 0 11 10"><path d="M1,5 L4,8.5 L10,1" fill="none" stroke="#fff" stroke-width="2"/></svg>bagging of the clippings<span class="features__note">(at an additional charge)</span></li>
      <li><svg width="11" height="10" viewBox="0 0 11 10"><path d="M1,5 L4,8.5 L10,1" fill="none" stroke="#fff" stroke-width="2"/></svg>dog waste clean-up.</li>
    </ul>
  </div>

  <p class="abs offer"><span class="offer__label">SPECIALOFFER:</span> <span class="offer__text">one free cut with commitment to a full 26 week season</span></p>
</section>

<section class="card card--back">
  <svg class="shapes" width="882" height="588" viewBox="0 0 882 588">
    <defs>
      <linearGradient id="gardenTone" x1="0" y1="0" x2="0" y2="1">
        <stop offset="0" stop-color="#f1f2ee"/>
        <stop offset="0.55" stop-color="#e8ece2"/>
        <stop offset="1" stop-color="#eef1ea"/>
      </linearGradient>
    </defs>
    <rect role="img" aria-label="Faded photo of a front garden with lawn and flower beds" width="882" height="588" fill="url(#gardenTone)"/>
    <path fill="var(--olive)" d="M0,120 C40,90 80,60 120,40 C60,120 20,220 0,330 Z"/>
    <path fill="var(--charcoal)" d="M0,0 L212,0 C130,30 60,80 0,125 Z"/>
    <path fill="var(--navy)" d="M705,588 C760,540 830,490 882,468 L882,588 Z"/>
    <circle cx="80" cy="86" r="50" fill="var(--charcoal)"/>
    <circle role="img" aria-label="Cartoon of Dawson riding his mower" cx="80" cy="86" r="43" fill="#2f7bbf"/>
  </svg>

  <div class="abs photo-slot">Your photo with mower</div>
  <div class="abs stamp">STAMP AREA</div>

  <div class="abs address">
    <div class="address__line">Recipient’s Name</div>
    <div class="address__line">Recipient’s Address</div>
    <div class="address__line">Contact no.</div>
    <div class="address__blank"></div>
  </div>

  <div class="abs" style="left:32px; top:357px;">
    <div class="wordmark">DAWSON MOWER</div>
    <div class="wordmark__school">MARWICK HIGH SCHOOL</div>
  </div>

  <div class="abs note-lines"><span></span><span></span><span></span><span></span></div>
</section>

</body>
</html>
```